Business Cards and Stationary Package
LedgerWise Partners, LLC
Use same font as used in my logo
Designer Discretion
Professional
Marta J. Hollis
President
418 Kestrel Lane
Cedar Hollow, GA 31599
mhollis@ledgerwise-partners.com
www.ledgerwise-partners.com
Please be creative, yet professional and simple.

```html
<!DOCTYPE html>
<html lang="en">
<head>
<meta charset="utf-8">
<title>LedgerWise Partners, LLC — Stationery</title>
<link href="https://fonts.googleapis.com/css2?family=Cinzel:wght@600&family=Open+Sans:wght@400;600&display=swap" rel="stylesheet">
<style>
  :root{
    --ink-blue:#1f4f9c;
    --band-blue:#1a63c4;
    --band-blue-light:#4fa3e8;
    --leaf:#5cb319;
    --leaf-dark:#2f8a0c;
    --leaf-light:#8fd43a;
    --paper:#ffffff;
    --shadow:rgba(0,0,0,.18);
    --text:#2b2b2b;
  }
  *{margin:0;padding:0;box-sizing:border-box}
  html,body{width:1200px;height:897px;overflow:hidden;background:#fff}
  .canvas{position:relative;width:1200px;height:897px;font-family:"Open Sans",Arial,sans-serif;color:var(--text)}
  .sheet{position:absolute;background:var(--paper);box-shadow:0 1px 5px var(--shadow);overflow:hidden}
  .sheet svg.band{position:absolute;left:0;bottom:0;display:block}
  .brand{position:absolute;display:flex;align-items:center;gap:8px}
  .brand-mark{width:30px;height:30px;background:var(--leaf);flex:none}
  .brand-name{font-family:"Cinzel",Georgia,serif;font-weight:600;color:var(--ink-blue);line-height:1;white-space:nowrap}
  .brand-name small{display:block;font-size:.42em;margin-top:3px;letter-spacing:.08em;text-align:center}
  .band-text{position:absolute;right:14px;color:#fff;text-align:right;white-space:nowrap}

  /* business card front */
  .card-front{left:360px;top:29px;width:197px;height:120px}
  .card-front .brand{left:10px;top:8px;gap:5px}
  .card-front .brand-mark{width:16px;height:16px}
  .card-front .brand-name{font-size:13px}
  .card-holder{position:absolute;left:10px;top:62px;font-size:7px;font-weight:600;line-height:1.3}
  .card-holder span{display:block;font-weight:400;font-size:5.5px}
  .card-contact{position:absolute;right:8px;top:52px;font-size:4.6px;line-height:1.45;color:#fff;text-align:right}

  /* business card back */
  .card-back{left:605px;top:29px;width:199px;height:120px;background:radial-gradient(circle at 50% 50%,var(--leaf-light),var(--leaf) 45%,var(--leaf-dark) 100%)}
  .card-back .ghost{position:absolute;inset:0;display:flex;align-items:center;justify-content:center;font-family:"Cinzel",Georgia,serif;font-weight:600;font-size:18px;color:rgba(255,255,255,.28)}

  /* letterhead */
  .letterhead{left:29px;top:206px;width:528px;height:665px}
  .letterhead .brand{left:150px;top:34px}
  .letterhead .brand-name{font-size:30px}
  .letterhead .band-text{bottom:34px;font-size:8px;line-height:1.55}
  .letterhead .web{position:absolute;right:14px;bottom:4px;font-size:8px;color:#fff}

  /* envelope front */
  .envelope{left:643px;top:206px;width:528px;height:262px}
  .envelope .brand{left:160px;top:34px}
  .envelope .brand-name{font-size:28px}
  .envelope .band-text{bottom:20px;font-size:8px}
  .envelope .web{position:absolute;right:14px;bottom:3px;font-size:8px;color:#fff}

  /* envelope back */
  .envelope-back{left:643px;top:511px;width:528px;height:360px}
  .envelope-back .flap{position:absolute;left:0;top:0;display:block}
  .envelope-back .ghost{position:absolute;left:0;right:0;top:38px;text-align:center;font-family:"Cinzel",Georgia,serif;font-weight:600;font-size:22px;color:rgba(255,255,255,.3)}
</style>
</head>
<body>
<div class="canvas">

  <section class="sheet card-front" aria-label="Business card front">
    <div class="brand"><div class="brand-mark"></div><div class="brand-name">LedgerWise<small>PARTNERS, LLC</small></div></div>
    <div class="card-holder">Marta J. Hollis<span>President</span></div>
    <svg class="band" width="197" height="82" viewBox="0 0 197 82">
      <defs><linearGradient id="cfBlue" x1="0" x2="1"><stop offset="0" stop-color="var(--band-blue-light)"/><stop offset="1" stop-color="var(--band-blue)"/></linearGradient></defs>
      <polygon points="110,0 197,0 197,72 80,72" fill="url(#cfBlue)"/>
      <polygon points="40,72 197,72 197,82 34,82" fill="var(--leaf)"/>
      <path d="M6,70 L12,78 L26,62" fill="none" stroke="var(--leaf)" stroke-width="3"/>
    </svg>
    <div class="card-contact">418 Kestrel Lane<br>Cedar Hollow, GA 31599<br>phone 555-010-0142<br>fax 555-010-0147<br>mhollis@ledgerwise-partners.com</div>
  </section>

  <section class="sheet card-back" aria-label="Business card back">
    <div class="ghost">LedgerWise</div>
  </section>

  <section class="sheet letterhead" aria-label="Letterhead">
    <div class="brand"><div class="brand-mark"></div><div class="brand-name">LedgerWise<small>PARTNERS, LLC</small></div></div>
    <svg class="band" width="528" height="75" viewBox="0 0 528 75">
      <defs><linearGradient id="lhBlue" x1="0" x2="1"><stop offset="0" stop-color="var(--band-blue-light)"/><stop offset=".5" stop-color="var(--band-blue)"/><stop offset="1" stop-color="var(--band-blue)"/></linearGradient></defs>
      <polygon points="120,8 528,0 528,58 60,58" fill="url(#lhBlue)"/>
      <polygon points="50,58 528,58 528,75 40,75" fill="var(--leaf)"/>
      <path d="M8,52 L20,68 L48,36" fill="none" stroke="var(--leaf)" stroke-width="5"/>
    </svg>
    <div class="band-text">P.O. Box 5120, Cedar Hollow, GA 31599<br>phone 555-010-0142, fax 555-010-0147, mhollis@ledgerwise-partners.com</div>
    <div class="web">www.ledgerwise-partners.com</div>
  </section>

  <section class="sheet envelope" aria-label="Envelope front">
    <div class="brand"><div class="brand-mark"></div><div class="brand-name">LedgerWise<small>PARTNERS, LLC</small></div></div>
    <svg class="band" width="528" height="50" viewBox="0 0 528 50">
      <defs><linearGradient id="evBlue" x1="0" x2="1"><stop offset="0" stop-color="var(--band-blue-light)"/><stop offset=".5" stop-color="var(--band-blue)"/><stop offset="1" stop-color="var(--band-blue)"/></linearGradient></defs>
      <polygon points="110,6 528,0 528,36 55,36" fill="url(#evBlue)"/>
      <polygon points="45,36 528,36 528,50 36,50" fill="var(--leaf)"/>
      <path d="M6,32 L16,45 L40,18" fill="none" stroke="var(--leaf)" stroke-width="4"/>
    </svg>
    <div class="band-text">P.O. Box 5120, Cedar Hollow, GA 31599</div>
    <div class="web">www.ledgerwise-partners.com</div>
  </section>

  <section class="sheet envelope-back" aria-label="Envelope back">
    <svg class="flap" width="528" height="140" viewBox="0 0 528 140">
      <defs><radialGradient id="flapGreen" cx=".5" cy=".3" r=".7"><stop offset="0" stop-color="var(--leaf-light)"/><stop offset=".5" stop-color="var(--leaf)"/><stop offset="1" stop-color="var(--leaf-dark)"/></radialGradient></defs>
      <path d="M0,0 H528 V110 Q520,122 500,124 H28 Q8,122 0,110 Z" fill="url(#flapGreen)"/>
    </svg>
    <div class="ghost">LedgerWise</div>
  </section>

</div>
</body>
</html>
```